Postcard Design January 2015

I need a postcard designed to introduce my company to potential new customers in the UK. My company is TW Page Services based in Chester and we represent one of Poland's leading and long established book printers. We offer competitive pricing, consistently high levels of print and binding quality and industry leading levels of customer service. We have been meeting the print requirements of UK publishers for more than 10 years.
Updates

Industry/Entity Type

Industry

```html
<!DOCTYPE html>
<html lang="en">
<head>
<meta charset="utf-8">
<title>TW Page Services – Postcard</title>
<link href="https://fonts.googleapis.com/css2?family=Arimo:wght@400;700&family=Oswald:wght@700&display=swap" rel="stylesheet">
<style>
  :root {
    --stage: #000000;
    --paper: #ffffff;
    --ink: #111111;
    --forest: #176b38;
    --leaf: #52b848;
    --highlight: #f2e619;
    --photo-grey-1: #f4f4f4;
    --photo-grey-2: #8a8a8a;
    --sky: #6d9fd6;
    --building: #c9c9c9;
  }
  * { box-sizing: border-box; margin: 0; padding: 0; }
  html, body {
    width: 947px; height: 1200px; overflow: hidden;
    background: var(--stage);
    font-family: "Arimo", Arial, sans-serif;
    color: var(--ink);
  }
  .card {
    position: absolute; left: 114px; width: 719px;
    background: var(--paper); overflow: hidden;
  }
  .card--front { top: 23px; height: 556px; }
  .card--back { top: 611px; height: 557px; }

  /* Front */
  .front-header { position: absolute; left: 0; top: 0; width: 100%; height: 146px; text-align: center; }
  .brand-title { position: absolute; top: 44px; width: 100%; font-size: 49px; font-weight: 700; letter-spacing: -0.5px; line-height: 1; }
  .brand-tagline { position: absolute; top: 98px; width: 100%; font-size: 27px; line-height: 1; letter-spacing: -0.3px; }

  .hero-photo {
    position: absolute; left: 0; top: 146px; width: 368px; height: 317px;
    background: radial-gradient(ellipse at 40% 45%, var(--photo-grey-1) 0%, #dcdcdc 55%, var(--photo-grey-2) 100%);
  }
  .hero-panel {
    position: absolute; left: 368px; top: 146px; width: 351px; height: 317px;
    background: var(--forest); color: var(--paper); padding: 22px 0 0 20px;
  }
  .hero-heading { font-size: 34px; line-height: 37px; font-weight: 400; }
  .hero-heading em { font-style: normal; font-weight: 700; color: var(--highlight); }
  .hero-body { margin-top: 22px; font-size: 21.5px; line-height: 24px; }
  .hero-cta { margin-top: 22px; font-size: 35px; line-height: 1; margin-left: -2px; }

  .contact-strip { position: absolute; left: 0; top: 463px; width: 100%; height: 93px; }
  .contact-strip__band { position: absolute; inset: 0; }
  .phone-big {
    position: absolute; left: 44px; top: 18px;
    display: flex; align-items: center; gap: 6px;
    font-family: "Oswald", "Arial Narrow", sans-serif; font-weight: 700;
    font-size: 42px; letter-spacing: -1px; line-height: 1;
  }
  .web-link {
    position: absolute; left: 390px; top: 29px;
    display: flex; align-items: center; gap: 9px;
    color: var(--paper); font-size: 21.5px;
  }

  /* Back */
  .info-panel {
    position: absolute; left: 0; top: 0; width: 347px; height: 331px;
    background: var(--forest); color: var(--paper); padding: 28px 0 0 37px;
  }
  .info-title { font-size: 22px; font-weight: 700; line-height: 1; }
  .info-tagline { font-size: 11.5px; margin-top: 4px; }
  .info-heading { font-size: 12.5px; font-weight: 700; margin-top: 15px; }
  .info-list { list-style: none; font-size: 12.4px; line-height: 16px; margin-top: 2px; padding-right: 16px; }
  .info-list li { padding-left: 13px; text-indent: -13px; }
  .info-heading--second { margin-top: 17px; }

  .factory-photo {
    position: absolute; left: 355px; top: 35px; width: 186px; height: 139px;
    background: linear-gradient(180deg, var(--sky) 0%, #b9d0ea 40%, var(--building) 45%, #9a9a9a 85%, #7a7a7a 100%);
  }
  .back-contact { position: absolute; left: 38px; top: 345px; font-size: 14px; line-height: 18px; }
  .back-contact__phone { font-size: 19.5px; margin-top: 10px; }
  .back-contact__lines { margin-top: 6px; font-size: 14px; line-height: 20px; }
</style>
</head>
<body>
  <section class="card card--front">
    <header class="front-header">
      <h1 class="brand-title">TW PAGE SERVICES</h1>
      <p class="brand-tagline">Litho &amp; Digital Printing, BookBinding &amp; Finishing</p>
    </header>

    <div class="hero-photo" role="img" aria-label="Black and white photo of an open book with fanned pages"></div>

    <div class="hero-panel">
      <h2 class="hero-heading">BOOK PRINTING<br>MADE <em>EASY</em></h2>
      <p class="hero-body">We offer a truly competitive service to book publishers looking for excellence in book printing and binding, combined with a first rate service.</p>
      <p class="hero-cta">Contact Us Today</p>
    </div>

    <div class="contact-strip">
      <svg class="contact-strip__band" viewBox="0 0 719 93" preserveAspectRatio="none" aria-hidden="true">
        <polygon points="400,0 719,0 719,93 304,93" fill="var(--leaf)"/>
      </svg>
      <div class="phone-big">
        <svg width="24" height="44" viewBox="0 0 24 44" aria-hidden="true">
          <path d="M9 2 C3 6 1 14 1 22 C1 30 3 38 9 42 L13 39 C14 38 14 37 13 36 L10 31 C9 30 8 30 7 31 C6 27 6 17 7 13 C8 14 9 14 10 13 L13 8 C14 7 14 6 13 5 Z" fill="var(--ink)"/>
        </svg>
        <span>01632 960418</span>
      </div>
      <div class="web-link">
        <svg width="28" height="28" viewBox="0 0 28 28" fill="none" stroke="var(--paper)" stroke-width="1.6" aria-hidden="true">
          <circle cx="14" cy="14" r="12.5"/>
          <ellipse cx="14" cy="14" rx="5.5" ry="12.5"/>
          <line x1="1.5" y1="14" x2="26.5" y2="14"/>
          <path d="M3.5 7.5 H24.5 M3.5 20.5 H24.5"/>
        </svg>
        <span>www.twpageservices.co.uk</span>
      </div>
    </div>
  </section>

  <section class="card card--back">
    <div class="info-panel">
      <h2 class="info-title">TW PAGE SERVICES</h2>
      <p class="info-tagline">Litho &amp; Digital Printing, BookBinding &amp; Finishing</p>

      <h3 class="info-heading">SERVICES</h3>
      <ol class="info-list">
        <li>1. High quality book printing and binding</li>
        <li>2. Competitive pricing</li>
        <li>3. Excellent customer service</li>
      </ol>

      <h3 class="info-heading info-heading--second">OTHER SERVICES</h3>
      <ol class="info-list">
        <li>1. We produce paperback and hardback books in mono or full colour. Binding options include &nbsp;sewn, perfect, Wiro-o and saddle stitched</li>
        <li>2. Print finishing includes lamination, spot UV and foil stamping</li>
        <li>3. We have state of the art production equipment, use top quality materials and follow strict quality control procedures</li>
        <li>4. We have weekly shipments in to the UK</li>
      </ol>
    </div>

    <div class="factory-photo" role="img" aria-label="Photo of the printing works building with flags under a blue sky"></div>

    <div class="back-contact">
      <p>Contact us for further<br>INFORMATION, QUOTATIONS or SAMPLES.</p>
      <p class="back-contact__phone">Phone - 01632 960418</p>
      <p class="back-contact__lines">Website - www.twpageservices.co.uk<br>Email - tomwade@twpageservices.co.uk</p>
    </div>
  </section>
</body>
</html>
```